Business Card Design

www.bellwaterridge.com.au

Bellwater Ridge Bed and Breakfast
A unique property with spectacular views situated in a peaceful quiet court surrounded by other quality homes. Set back from the street, this wonderful residence has plenty of space. The huge paved driveway has tonnes of off street parking

Relax in the beautifully landscaped lawn area with mature trees. The stunning balcony & deck is an ideal place to sit & watch the spectacular sunsets through the tree tops. Just wonderful!

The self-contained Bed and Breakfast has its own separate entrance door and consists of a large lounge/ kitchenette with sink & a separate bedroom. The bathroom has a glass shower screen, toilet & vanity unit.
If you are looking for your own piece of paradise in an ideal established setting with plenty of room then you must stay at Bellwater ridge
This really is a slice of Heaven so come & stay!

- Established landscaped gardens & lawn areas
- paved driveway - loads of off street parking
- Splendid balcony with glorious views
- Close to shopping & transport

We welcome you to relax and unwind in the charm of our modern country feel bed and breakfast in the Northern Suburbs of Adelaide, offering privacy and relaxation, it is perfect for couples
This self-contained bed & breakfast will provide you with a “home away from home”, including breakfast provisions and all the comfort and modern conveniences you’d expect Bellwater Ridge is perfect whether you’re on a holiday visit to Adelaide or here for business.
Enjoy the many activities Adelaide has to offer, we are positioned in the Northern Suburbs for you to easily travel to the Adelaide Hills or Barossa Wine region.
Bellwater Ridge B & B is in a fantastic location for whatever you want to do on your visit to South Australia. Nestled within walking distance to the Cobbler Creek or visit our world renowned wine regions. Of course, we can help and point you in the right direction.

Shopping

14 Bellwater Court
Larkfield Heights LF 4821

Dennis & Maureen Pellham
0412 555 648 or 0413 555 927
www.bellwaterridge.com.au
dennis@bellwaterridge.com.au

```html
<!DOCTYPE html>
<html lang="en">
<head>
<meta charset="utf-8">
<title>Bellwater Ridge Bed and Breakfast – Business Card</title>
<link rel="stylesheet" href="https://fonts.googleapis.com/css2?family=EB+Garamond&family=Pinyon+Script&display=swap">
<style>
  :root {
    --page: #ffffff;
    --card-cream: #fef0c8;
    --glow-large: #fff8e6;
    --glow-peach: rgba(251, 216, 205, 0.5);
    --glow-rose: rgba(226, 200, 200, 0.55);
    --rule: #7a6f60;
    --ink: #111111;
  }
  html, body {
    margin: 0;
    padding: 0;
    width: 1200px;
    height: 603px;
    overflow: hidden;
    background: var(--page);
  }
  .card {
    position: relative;
    width: 1063px;
    height: 603px;
    background: var(--card-cream);
    overflow: hidden;
  }
  .card-decor {
    position: absolute;
    inset: 0;
  }
  .business-name {
    position: absolute;
    left: 137px;
    top: 110px;
    margin: 0;
    font-family: "Pinyon Script", cursive;
    font-weight: 400;
    font-size: 56px;
    line-height: 1;
    color: var(--ink);
    white-space: nowrap;
  }
  .contact {
    position: absolute;
    left: 137px;
    margin: 0;
    font-family: "EB Garamond", serif;
    font-size: 27px;
    letter-spacing: 0.4px;
    line-height: 32.5px;
    color: var(--ink);
    font-style: normal;
    white-space: nowrap;
  }
  .contact-details { top: 213px; }
  .contact-online { top: 364px; line-height: 30px; }
  .contact span { display: block; }
</style>
</head>
<body>
  <div class="card">
    <svg class="card-decor" width="1063" height="603" viewBox="0 0 1063 603" aria-hidden="true">
      <circle class="glow-large" cx="299" cy="300" r="374" fill="var(--glow-large)"/>
      <circle class="glow-peach" cx="735" cy="230" r="192" fill="var(--glow-peach)"/>
      <circle class="glow-rose" cx="905" cy="367" r="105" fill="var(--glow-rose)"/>
      <line class="rule-vertical" x1="115.5" y1="92" x2="115.5" y2="498" stroke="var(--rule)" stroke-width="1"/>
      <line class="rule-horizontal" x1="72" y1="471.5" x2="711" y2="471.5" stroke="var(--rule)" stroke-width="1"/>
    </svg>

    <h1 class="business-name">Bellwater Ridge Bed and Breakfast</h1>

    <address class="contact contact-details">
      <span>14 Bellwater Court Larkfield Heights LF 4821</span>
      <span>Dennis &amp; Maureen Pellham</span>
      <span>0412 555 648 or 0413 555 927</span>
    </address>

    <address class="contact contact-online">
      <span>dennis@bellwaterridge.com.au</span>
      <span>www.bellwaterridge.com.au</span>
    </address>
  </div>
</body>
</html>
```